Corvid Lens Studio Business Card Design

I need a business card designed for a photography business based in Perth, Western Australia called Corvid Lens Studio.

We specialise in wedding, event photography and portrait photography.

The business card must borrow the style of the attached logo.

The hex codes for the colours in the logo are:
#ED1D85 - Pink
#89C23E - Green
#37282F - Black

The name on the card will be:
Name: Tobiah
Phone: 0417395268
Website: www.corvidlensstudio.com.au
Facebook: corvidlensstudio

I am open and happy to accept creative concepts.

Industry/Entity Type

Business

```html
<!DOCTYPE html>
<html lang="en">
<head>
<meta charset="utf-8">
<title>Corvid Lens Studio — Business Card</title>
<link rel="stylesheet" href="https://fonts.googleapis.com/css2?family=Questrial&display=swap">
<style>
  :root {
    --pink: #ED1D85;
    --green: #89C23E;
    --ink: #37282F;
    --paper: #ffffff;
    --backdrop: #eeeeef;
    --card-shadow: rgba(55, 40, 47, 0.14);
  }
  * { box-sizing: border-box; margin: 0; padding: 0; }
  html, body {
    width: 1200px;
    height: 720px;
    overflow: hidden;
    background: var(--backdrop);
    font-family: "Questrial", "Century Gothic", sans-serif;
    color: var(--ink);
  }
  .sheet {
    position: relative;
    width: 1200px;
    height: 720px;
    display: flex;
    align-items: center;
    justify-content: center;
    gap: 60px;
  }
  .card {
    width: 500px;
    height: 286px;
    background: var(--paper);
    border-radius: 3px;
    box-shadow: 0 2px 3px var(--card-shadow), 0 12px 30px var(--card-shadow);
    position: relative;
  }

  /* Front */
  .card-front {
    display: flex;
    align-items: center;
    justify-content: center;
    gap: 16px;
  }
  .brand-dot {
    width: 22px;
    height: 22px;
    border-radius: 50%;
    background: var(--pink);
    flex: none;
  }
  .brand-name {
    font-size: 15px;
    letter-spacing: 0.42em;
    text-transform: uppercase;
    color: var(--ink);
  }

  /* Back */
  .card-back {
    display: flex;
    align-items: center;
    padding-left: 46px;
  }
  .back-mark {
    width: 108px;
    display: flex;
    flex-direction: column;
    align-items: center;
    gap: 8px;
  }
  .back-mark .brand-dot { width: 40px; height: 40px; }
  .back-mark .brand-name-small {
    font-size: 10px;
    letter-spacing: 0.18em;
    text-transform: uppercase;
    color: var(--ink);
    text-align: center;
    line-height: 1.4;
  }
  .divider {
    width: 1.5px;
    height: 80px;
    background: var(--ink);
    margin: 0 22px 0 26px;
  }
  .contact { line-height: 1.15; }
  .contact .person-name {
    font-size: 19px;
    color: var(--green);
  }
  .contact .role {
    font-size: 13px;
    color: var(--pink);
    margin-bottom: 5px;
  }
  .contact .detail {
    font-size: 13.5px;
    color: var(--ink);
    letter-spacing: 0.01em;
  }
  .contact .detail-gap { margin-top: 4px; }
</style>
</head>
<body>
  <main class="sheet">
    <section class="card card-front" aria-label="Card front">
      <span class="brand-dot"></span>
      <span class="brand-name">Corvid Lens Studio</span>
    </section>

    <section class="card card-back" aria-label="Card back">
      <div class="back-mark">
        <span class="brand-dot"></span>
        <span class="brand-name-small">Corvid Lens Studio</span>
      </div>
      <div class="divider"></div>
      <div class="contact">
        <p class="person-name">Tobiah</p>
        <p class="role">Photographer</p>
        <p class="detail">0417395268</p>
        <p class="detail">www.corvidlensstudio.com.au</p>
        <p class="detail detail-gap">Facebook: corvidlensstudio</p>
      </div>
    </section>
  </main>
</body>
</html>
```